Example of School Sign for Digital Siganage

We sell digital signage software and screens. I have an expo coming up and I want some examples of typical images and messages that a school might use on an outdoor screen for public viewing. The resolution of the screen is quite low at 504 pixels wide by 336 pixels high. This means that we cannot use anything too small or detailed. The images could however be created at 1008 x 672 and that way they will scale down. The images need to be delivered in .psd format with all layers available.

We will call the School Stonemere Heights College. We want the school name on all the images (slides) and a fictitious logo associated with the name. Examples of the images required would be. . .

1. Congratulations to Lucy Pembridge School Dux 2015. (This would have an image of a smiling teenage girl.)

2. Team of the Week. Year 10 Girls under 16 Soccer Team. 5-Wins 0-Losses. (This would have a picture of girls playing soccer.)

3. School Production of Brassline. August 12th -17th. Get your tickets from the office . (An image of a Brassline logo)

4. Car Wash at School the Sunday to raise funds for the Year 9 Singapore Trip. (Image of students washing a car)

5. School Holidays Start Friday the 8th of September. School re-opens Monday 25th of September. (An image of a crowd of happy students)

6. Student of the Week. Tobin Walsh, Winner of the Meridian Automaton Shield. (image of teenage student with robot)

Hopefully this is clear.

Industry/Entity Type

Digital Signage

Font styles to use
Sans Serif

Requirements
Must have
• School Name and Logo
Should not have
• Any very small fonts or too much fine detail

```html
<!DOCTYPE html>
<html lang="en">
<head>
<meta charset="utf-8">
<title>Stonemere Heights College – Signage Slides</title>
<link rel="stylesheet" href="https://fonts.googleapis.com/css2?family=Roboto+Condensed:wght@700&family=Fredoka:wght@600&display=swap">
<style>
  :root {
    --stage: #231f20;
    --white: #ffffff;
    --purple-deep: #5b2c90;
    --purple-bright: #8c2a9c;
    --lilac-text: #c8b2e4;
    --green-deep: #08a443;
    --green-light: #63c95b;
    --yellow: #ffec00;
    --wave-blue: #0a9fd4;
    --wave-blue-dark: #0b7bc0;
    --sponsor-lilac: #d6a6d8;
    --school-navy: #1d3a6e;
    --photo-warm: #d9b59a;
    --photo-cool: #b9a6cf;
    --photo-red: #c9303a;
  }
  * { box-sizing: border-box; margin: 0; padding: 0; }
  html, body { width: 864px; height: 1200px; overflow: hidden; background: var(--stage); }
  body { position: relative; font-family: "Roboto Condensed", Arial, sans-serif; }

  .slide {
    position: absolute; left: 82px; width: 696px; height: 464px; overflow: hidden;
  }
  .slide--dux { top: 91px; background: linear-gradient(90deg, var(--purple-deep), var(--purple-bright)); }
  .slide--team { top: 640px; background: radial-gradient(ellipse at 60% 45%, var(--green-light), var(--green-deep) 70%); }

  .photo { position: absolute; left: 0; top: 0; width: 696px; height: 464px; }
  .photo__part { position: absolute; }
  .slide--dux .photo__head {
    left: 490px; top: 14px; width: 110px; height: 200px; border-radius: 50% 50% 20px 20px;
    background: var(--photo-warm);
  }
  .slide--dux .photo__body {
    left: 396px; top: 170px; width: 272px; height: 200px; border-radius: 40px 40px 0 0;
    background: linear-gradient(180deg, var(--photo-warm), var(--photo-cool));
  }
  .slide--team .photo__head {
    left: 518px; top: 12px; width: 92px; height: 140px; border-radius: 50% 50% 20px 20px;
    background: var(--photo-warm);
  }
  .slide--team .photo__body {
    left: 430px; top: 128px; width: 238px; height: 240px; border-radius: 40px 40px 0 0;
    background: linear-gradient(180deg, var(--photo-warm), var(--photo-red) 45%);
  }

  .slide__wave { position: absolute; left: 0; top: 0; width: 696px; height: 464px; }

  .slide__headline {
    position: absolute; left: 37px; top: 66px;
    color: var(--white); font-size: 48px; font-weight: 700; line-height: 1;
  }
  .slide__message {
    position: absolute; left: 38px; top: 122px;
    font-size: 32px; font-weight: 700; line-height: 39px;
  }
  .slide--dux .slide__message { color: var(--lilac-text); }
  .slide--team .slide__message { color: var(--yellow); font-size: 30px; line-height: 37px; }

  .sponsor {
    position: absolute; left: 20px; top: 350px; width: 220px; text-align: center;
    font-family: "Fredoka", Arial, sans-serif; font-weight: 600; color: var(--sponsor-lilac);
    font-size: 22px; line-height: 33px;
  }
  .sponsor__url { font-size: 20px; }

  .school-name {
    position: absolute; left: 438px; top: 393px;
    color: var(--school-navy); font-size: 24px; font-weight: 700; line-height: 26px;
    display: flex; align-items: center; gap: 10px;
  }
  .school-name__mark { width: 16px; height: 16px; border-radius: 50%; background: var(--school-navy); flex: none; }
  .school-name__sub { display: block; font-size: 17px; line-height: 20px; }
</style>
</head>
<body>

<section class="slide slide--dux">
  <div class="photo" role="img" aria-label="Photo of a smiling teenage student holding folders">
    <div class="photo__part photo__head" aria-hidden="true"></div>
    <div class="photo__part photo__body" aria-hidden="true"></div>
  </div>
  <svg class="slide__wave" viewBox="0 0 696 464" aria-hidden="true">
    <path d="M0 318 C140 278 300 312 430 350 C540 380 620 330 696 300 L696 464 L0 464Z" fill="var(--wave-blue)"/>
    <path d="M0 334 C140 296 300 330 430 366 C540 394 620 346 696 316 L696 464 L0 464Z" fill="var(--white)"/>
  </svg>
  <h1 class="slide__headline">CONGRATULATIONS</h1>
  <p class="slide__message">TO LUCY PEMBRIDGE SCHOOL<br>DUX 2015</p>
  <div class="sponsor">HERE IS<br>COMPANY LOGO<br><span class="sponsor__url">www.sponsorsite.org</span></div>
  <div class="school-name"><span class="school-name__mark"></span><span>STONEMERE HEIGHTS<span class="school-name__sub">Community College</span></span></div>
</section>

<section class="slide slide--team">
  <div class="photo" role="img" aria-label="Photo of a girl in a red soccer kit holding a soccer ball">
    <div class="photo__part photo__head" aria-hidden="true"></div>
    <div class="photo__part photo__body" aria-hidden="true"></div>
  </div>
  <svg class="slide__wave" viewBox="0 0 696 464" aria-hidden="true">
    <path d="M0 318 C140 278 300 312 430 350 C540 380 620 330 696 300 L696 464 L0 464Z" fill="var(--wave-blue-dark)"/>
    <path d="M0 334 C140 296 300 330 430 366 C540 394 620 346 696 316 L696 464 L0 464Z" fill="var(--white)"/>
  </svg>
  <h1 class="slide__headline">TEAM OF THE WEEK.</h1>
  <p class="slide__message">YEAR 10 GIRLS UNDER 16<br>SOCCER TEAM.<br>5-WINS 0-LOSSES.</p>
  <div class="sponsor">HERE IS<br>COMPANY LOGO<br><span class="sponsor__url">www.sponsorsite.org</span></div>
  <div class="school-name"><span class="school-name__mark"></span><span>STONEMERE HEIGHTS<span class="school-name__sub">Community College</span></span></div>
</section>

</body>
</html>
```